Stationary / Envelopes / Cards
Project: Business Card Design
Business Card Design
Use specific fonts
You can use the same font as the logo or similar fonts, I am up for anything that goes
Professional
Colin Hartwell
Director of IT Consulting
PO Box XXXX Millbrook RI 02741
hartwellcd@brightlanetec.com
www.brightlanetec.com
The address on the brief will be updated in the next few days.
I would like to leave this design element up to you. I don't want to limit your creativity.

```html
<!DOCTYPE html>
<html lang="en">
<head>
<meta charset="utf-8">
<title>Brightlane Tech – Stationery Set</title>
<link href="https://fonts.googleapis.com/css2?family=Roboto:wght@400;500;700&display=swap" rel="stylesheet">
<style>
  :root{
    --bg:#d9d6d1;
    --paper:#ffffff;
    --navy:#1c1f86;
    --blue:#2b36b8;
    --bright:#1f78e6;
    --sky:#4fa3f2;
    --ink:#2a2d4a;
    --muted:#7b7f95;
    --silver:#c9ccd3;
    --silver-dark:#9a9ea8;
  }
  *{box-sizing:border-box;margin:0;padding:0}
  html,body{width:1200px;height:886px;overflow:hidden}
  body{background:var(--bg);font-family:"Roboto",Arial,sans-serif;color:var(--ink);position:relative}
  .piece{position:absolute;background:var(--paper);box-shadow:0 3px 8px rgba(0,0,0,.25);overflow:hidden}
  .piece svg.art{position:absolute;inset:0;width:100%;height:100%}

  .brand{position:absolute;display:flex;align-items:center;gap:6px;font-weight:700;color:var(--navy);white-space:nowrap;line-height:1}
  .brand .dot{border-radius:50%;background:var(--navy);flex:none}
  .brand.sm{font-size:13px}.brand.sm .dot{width:18px;height:18px}
  .brand.md{font-size:16px}.brand.md .dot{width:24px;height:24px}
  .brand.light{color:#fff}.brand.light .dot{background:#fff}

  .address{position:absolute;font-size:9px;color:var(--ink);white-space:nowrap}
  .address.light{color:#fff}

  .contact{position:absolute;list-style:none;font-size:6.5px;line-height:11px;color:var(--ink)}
  .contact li{display:flex;align-items:center;gap:4px;white-space:nowrap}
  .contact li::before{content:"";width:5px;height:5px;border-radius:50%;background:var(--blue);flex:none}
  .contact.light{color:#fff}.contact.light li::before{background:#fff}

  .person{position:absolute;line-height:1.25}
  .person .name{font-size:9px;font-weight:700}
  .person .role{font-size:6.5px}
  .person.light{color:#fff}

  .footer-line{position:absolute;font-size:6.5px;color:var(--ink);white-space:nowrap}

  /* placement */
  .env-front{left:43px;top:34px;width:348px;height:175px}
  .env-plain{left:43px;top:216px;width:348px;height:140px}
  .env-back{left:43px;top:360px;width:348px;height:163px}
  .env-silver{left:43px;top:528px;width:348px;height:168px}
  .letter-a{left:403px;top:34px;width:360px;height:554px}
  .letter-b{left:780px;top:34px;width:360px;height:554px}
  .card{width:245px;height:108px}
  .c1{left:408px;top:605px}.c2{left:665px;top:605px}.c3{left:924px;top:605px}
  .c4{left:408px;top:732px}.c5{left:665px;top:732px}.c6{left:924px;top:732px}
</style>
</head>
<body>

<!-- Envelope front with diagonal band -->
<section class="piece env-front">
  <svg class="art" viewBox="0 0 348 175" preserveAspectRatio="none">
    <defs><linearGradient id="band" x1="0" y1="0" x2="1" y2="1"><stop offset="0" stop-color="#2b36b8"/><stop offset="1" stop-color="#1c1f86"/></linearGradient></defs>
    <polygon points="196,0 348,0 348,175 120,175" fill="url(#band)"/>
    <polygon points="190,0 196,0 120,175 114,175" fill="#4fa3f2"/>
  </svg>
  <div class="brand sm" style="left:14px;top:14px"><span class="dot"></span>Brightlane Tech</div>
  <p class="address light" style="left:160px;top:130px">PO Box XXXX Millbrook RI 02741</p>
</section>

<!-- Envelope front, plain -->
<section class="piece env-plain">
  <svg class="art" viewBox="0 0 348 140" preserveAspectRatio="none">
    <rect x="0" y="124" width="348" height="3" fill="#c9ccd3"/>
  </svg>
  <div class="brand sm" style="left:14px;top:14px"><span class="dot"></span>Brightlane Tech</div>
  <p class="address" style="left:14px;top:104px">PO Box XXXX Millbrook RI 02741</p>
</section>

<!-- Envelope back, blue flap -->
<section class="piece env-back">
  <svg class="art" viewBox="0 0 348 163" preserveAspectRatio="none">
    <defs><linearGradient id="flap" x1="0" y1="0" x2="0" y2="1"><stop offset="0" stop-color="#1c1f86"/><stop offset="1" stop-color="#2b36b8"/></linearGradient></defs>
    <polygon points="0,0 348,0 348,18 174,80 0,18" fill="url(#flap)"/>
    <polyline points="0,18 174,80 348,18" fill="none" stroke="#4fa3f2" stroke-width="2"/>
  </svg>
  <div class="brand sm light" style="left:124px;top:32px"><span class="dot"></span>Brightlane Tech</div>
</section>

<!-- Envelope back, silver flap -->
<section class="piece env-silver">
  <svg class="art" viewBox="0 0 348 168" preserveAspectRatio="none">
    <defs><linearGradient id="metal" x1="0" y1="0" x2="0" y2="1"><stop offset="0" stop-color="#9a9ea8"/><stop offset="1" stop-color="#dfe1e6"/></linearGradient></defs>
    <polygon points="0,0 348,0 348,20 174,72 0,20" fill="url(#metal)"/>
  </svg>
  <div class="brand sm" style="left:124px;top:20px"><span class="dot"></span>Brightlane Tech</div>
</section>

<!-- Letterhead A -->
<section class="piece letter-a">
  <svg class="art" viewBox="0 0 360 554" preserveAspectRatio="none">
    <path d="M0,540 L300,540 Q330,540 360,518 L360,554 L0,554 Z" fill="#1c1f86"/>
    <path d="M0,536 L300,536 Q330,536 360,514 L360,518 Q330,540 300,540 L0,540 Z" fill="#4fa3f2"/>
  </svg>
  <div class="brand md" style="left:20px;top:20px"><span class="dot"></span>Brightlane Tech</div>
  <ul class="contact" style="left:196px;top:18px">
    <li>PO Box XXXX</li>
    <li>Millbrook RI 02741</li>
    <li>401 555 0147</li>
    <li>hartwellcd@brightlanetec.com</li>
  </ul>
</section>

<!-- Letterhead B -->
<section class="piece letter-b">
  <svg class="art" viewBox="0 0 360 554" preserveAspectRatio="none">
    <rect x="0" y="544" width="360" height="10" fill="#1c1f86"/>
    <rect x="0" y="541" width="360" height="3" fill="#4fa3f2"/>
  </svg>
  <div class="brand md" style="left:112px;top:22px"><span class="dot"></span>Brightlane Tech</div>
  <p class="footer-line" style="left:110px;top:512px">PO Box XXXX Millbrook RI 02741</p>
  <p class="footer-line" style="left:70px;top:524px">401 555 0147 · hartwellcd@brightlanetec.com · www.brightlanetec.com</p>
</section>

<!-- Business card, blue front with details -->
<section class="piece card c1">
  <svg class="art" viewBox="0 0 245 108" preserveAspectRatio="none">
    <defs><linearGradient id="cardblue" x1="0" y1="0" x2="1" y2="1"><stop offset="0" stop-color="#1c1f86"/><stop offset=".6" stop-color="#2b36b8"/><stop offset="1" stop-color="#1f78e6"/></linearGradient></defs>
    <rect width="245" height="108" fill="url(#cardblue)"/>
    <path d="M0,96 Q120,80 245,92 L245,108 L0,108 Z" fill="#4fa3f2" opacity=".5"/>
  </svg>
  <div class="brand sm light" style="left:12px;top:10px"><span class="dot"></span>Brightlane Tech</div>
  <div class="person light" style="left:12px;top:42px"><p class="name">Colin Hartwell</p><p class="role">Director of IT Consulting</p></div>
  <ul class="contact light" style="left:12px;top:66px">
    <li>401 555 0147</li>
    <li>hartwellcd@brightlanetec.com</li>
  </ul>
</section>

<!-- Business card, white front -->
<section class="piece card c2">
  <svg class="art" viewBox="0 0 245 108" preserveAspectRatio="none">
    <rect x="0" y="98" width="245" height="10" fill="#2b36b8"/>
    <rect x="0" y="95" width="245" height="3" fill="#4fa3f2"/>
  </svg>
  <div class="brand sm" style="left:12px;top:10px"><span class="dot"></span>Brightlane Tech</div>
  <div class="person" style="left:12px;top:44px"><p class="name">Colin Hartwell</p><p class="role">Director of IT Consulting</p></div>
  <ul class="contact" style="left:120px;top:40px">
    <li>401 555 0147</li>
    <li>hartwellcd@brightlanetec.com</li>
    <li>www.brightlanetec.com</li>
  </ul>
</section>

<!-- Business card, blue back -->
<section class="piece card c3">
  <svg class="art" viewBox="0 0 245 108" preserveAspectRatio="none">
    <rect width="245" height="108" fill="url(#cardblue)"/>
  </svg>
  <div class="brand md light" style="left:56px;top:42px"><span class="dot"></span>Brightlane Tech</div>
</section>

<!-- Business card, blue front variant -->
<section class="piece card c4">
  <svg class="art" viewBox="0 0 245 108" preserveAspectRatio="none">
    <rect width="245" height="108" fill="url(#cardblue)"/>
    <path d="M0,96 Q120,80 245,92 L245,108 L0,108 Z" fill="#4fa3f2" opacity=".5"/>
  </svg>
  <div class="brand md light" style="left:12px;top:12px"><span class="dot"></span>Brightlane Tech</div>
  <div class="person light" style="left:12px;top:48px"><p class="name">Colin Hartwell</p><p class="role">Director of IT Consulting</p></div>
  <ul class="contact light" style="left:130px;top:48px">
    <li>401 555 0147</li>
    <li>www.brightlanetec.com</li>
  </ul>
</section>

<!-- Business card, white front variant -->
<section class="piece card c5">
  <svg class="art" viewBox="0 0 245 108" preserveAspectRatio="none">
    <rect x="0" y="98" width="245" height="10" fill="#2b36b8"/>
    <rect x="0" y="95" width="245" height="3" fill="#4fa3f2"/>
  </svg>
  <div class="brand sm" style="left:12px;top:10px"><span class="dot"></span>Brightlane Tech</div>
  <div class="person" style="left:12px;top:44px"><p class="name">Colin Hartwell</p><p class="role">PO Box XXXX Millbrook RI 02741</p></div>
  <ul class="contact" style="left:130px;top:40px">
    <li>401 555 0147</li>
    <li>hartwellcd@brightlanetec.com</li>
    <li>www.brightlanetec.com</li>
  </ul>
</section>

<!-- Business card, blue back variant -->
<section class="piece card c6">
  <svg class="art" viewBox="0 0 245 108" preserveAspectRatio="none">
    <rect width="245" height="108" fill="url(#cardblue)"/>
  </svg>
  <div class="brand md light" style="left:56px;top:42px"><span class="dot"></span>Brightlane Tech</div>
</section>

</body>
</html>
```